Pet Sitting Business Card

Would like a business card designed for my new pet sitting business
Card needs to match with logo design.
Blue and Orange are the theme colours.

Simple yet sophisticated design

company name:- MARIGOLD PET CARE
Dana Corbel
Owner
0472615390
dana@marigoldpetcare.com.au
www.marigoldpetcare.com.au

I'm going to close my deadline early. I will be picking a winner by the 10th of May. Please submit designs before then.
thank you

Target Market(s)

All types of professional pet lovers wishing to have their pet looked after

Industry/Entity Type

Pet

Requirements
Must have
• Logo design
Blue and orange

```html
<!DOCTYPE html>
<html lang="en">
<head>
<meta charset="utf-8">
<title>Marigold Pet Care – Business Card</title>
<link rel="stylesheet" href="https://fonts.googleapis.com/css2?family=Oswald:wght@500;600&family=Exo+2:wght@400;500&display=swap">
<style>
  :root {
    --blue: #1f8fe8;
    --orange: #ef8a1f;
    --white: #ffffff;
    --ink: #1d1d1d;
    --backdrop: #e9e6e1;
  }
  * { margin: 0; padding: 0; box-sizing: border-box; }
  html, body { width: 1200px; height: 987px; overflow: hidden; background: var(--backdrop); }
  .canvas { position: relative; width: 1200px; height: 987px; }
  .card {
    position: absolute; top: 113px; width: 420px; height: 760px;
    background: var(--white); overflow: hidden;
    box-shadow: 0 6px 18px rgba(0,0,0,.18);
  }
  .card--back { left: 150px; }
  .card--front { left: 630px; }
  .card__shapes { position: absolute; inset: 0; width: 100%; height: 100%; }
  .shape-blue { fill: var(--blue); }
  .shape-orange { fill: var(--orange); }
  .brand {
    position: absolute; left: 0; right: 0; text-align: center;
    font-family: "Oswald", sans-serif; font-weight: 600;
    color: var(--blue); letter-spacing: 2px; line-height: 1.05;
  }
  .card--back .brand { top: 250px; font-size: 40px; }
  .card--front .brand { top: 70px; font-size: 30px; }
  .person { position: absolute; left: 60px; right: 40px; top: 205px; text-align: right; }
  .person__name {
    font-family: "Oswald", sans-serif; font-weight: 500; font-size: 30px;
    letter-spacing: 1px; color: var(--ink); text-transform: uppercase;
  }
  .person__role {
    font-family: "Exo 2", sans-serif; font-size: 15px; letter-spacing: 3px;
    color: var(--ink); text-transform: uppercase; margin-top: 2px;
  }
  .contacts {
    position: absolute; left: 22px; right: 18px; top: 318px;
    display: flex; justify-content: space-between; gap: 10px;
    font-family: "Exo 2", sans-serif; font-size: 11.5px; color: var(--ink);
  }
  .contacts__col { display: flex; flex-direction: column; gap: 12px; }
  .contact { display: flex; align-items: center; gap: 6px; white-space: nowrap; }
  .contact__icon { width: 16px; height: 16px; flex: none; }
  .contact__icon circle { fill: none; stroke: var(--ink); stroke-width: 1.4; }
  .contact__icon path { fill: var(--ink); }
  .address {
    position: absolute; left: 0; right: 0; top: 570px; text-align: center;
    font-family: "Exo 2", sans-serif; font-size: 15px; letter-spacing: 1.5px;
    color: var(--white); line-height: 1.7;
  }
  .address__pin { width: 30px; height: 30px; display: block; margin: 0 auto 14px; }
</style>
</head>
<body>
<main class="canvas">

  <section class="card card--back" aria-label="Card back">
    <svg class="card__shapes" viewBox="0 0 420 760" aria-hidden="true">
      <polygon class="shape-orange" points="0,0 420,0 420,24 210,8 0,24"/>
      <polygon class="shape-orange" points="0,452 210,522 420,452 420,472 210,542 0,472"/>
      <polygon class="shape-blue" points="0,472 210,542 420,472 420,760 0,760"/>
    </svg>
    <div class="brand">MARIGOLD<br>PET CARE</div>
  </section>

  <section class="card card--front" aria-label="Card front">
    <svg class="card__shapes" viewBox="0 0 420 760" aria-hidden="true">
      <polygon class="shape-orange" points="0,0 420,0 420,24 210,8 0,24"/>
      <polygon class="shape-orange" points="0,452 210,522 420,452 420,472 210,542 0,472"/>
      <polygon class="shape-blue" points="0,472 210,542 420,472 420,760 0,760"/>
    </svg>

    <div class="brand">MARIGOLD<br>PET CARE</div>

    <div class="person">
      <div class="person__name">Dana Corbel</div>
      <div class="person__role">Owner</div>
    </div>

    <div class="contacts">
      <div class="contacts__col">
        <div class="contact">
          <svg class="contact__icon" viewBox="0 0 16 16" aria-hidden="true"><circle cx="8" cy="8" r="7"/><path d="M5.5 4.5l1.5-.5 1 2-1 1a5 5 0 0 0 2 2l1-1 2 1-.5 1.5c-3 .5-6.5-3-6-6z"/></svg>
          <span>0472615390</span>
        </div>
        <div class="contact">
          <svg class="contact__icon" viewBox="0 0 16 16" aria-hidden="true"><circle cx="8" cy="8" r="7"/><path d="M5.5 4.5l1.5-.5 1 2-1 1a5 5 0 0 0 2 2l1-1 2 1-.5 1.5c-3 .5-6.5-3-6-6z"/></svg>
          <span>0472615390</span>
        </div>
      </div>
      <div class="contacts__col">
        <div class="contact">
          <svg class="contact__icon" viewBox="0 0 16 16" aria-hidden="true"><circle cx="8" cy="8" r="7"/><path d="M4.5 5.5h7v5h-7z M4.5 5.5l3.5 2.5 3.5-2.5" fill="none" stroke="#1d1d1d"/></svg>
          <span>dana@marigoldpetcare.com.au</span>
        </div>
        <div class="contact">
          <svg class="contact__icon" viewBox="0 0 16 16" aria-hidden="true"><circle cx="8" cy="8" r="7"/><circle cx="8" cy="8" r="4"/><path d="M4 7.6h8v.8H4z"/></svg>
          <span>www.marigoldpetcare.com.au</span>
        </div>
      </div>
    </div>

    <div class="address">
      <svg class="address__pin" viewBox="0 0 30 30" aria-hidden="true">
        <circle cx="15" cy="15" r="14" fill="none" stroke="#ffffff" stroke-width="1.6"/>
        <path d="M15 7a5 5 0 0 0-5 5c0 4 5 10 5 10s5-6 5-10a5 5 0 0 0-5-5zm0 7a2 2 0 1 1 0-4 2 2 0 0 1 0 4z" fill="#ffffff"/>
      </svg>
      214 Harbour Lane<br>2nd Floor Suite B
    </div>
  </section>

</main>
</body>
</html>
```